POS Systems

Redesign existing site with improvement in layout an sitemap

I need Responsive PSD Designs

Current site is http://brindlecheckout.com.au/

Client is no longer selling Cash Registers

Only doing Touch Screen Point of Sale Systems
for 4 main industries (Restaurants and Cafes, Grocery and Convenience, Fruit & Veg, Bars, Pubs and Clubs)

Sitemap:

1. Home - With 4 types of businesses serviced, 4 Video Testimonials, End Of Financial Year Sale, Finance Options

2. Our System - Video, text, Boxes of 4 Different Industries, Book a Consultation / Call
Drop down menu for each different industry

(Restaurants and Cafes, Grocery and Convenience, Fruit & Veg, Bars, Pubs and Clubs)

3. About Us - text about history

4. Events

5. Testimonials

6. News - blog page

7. Gallery

8. Contact

#I need PSD Files and I will convert to Wordpress Myself

#I need the Each page designed please except Gallery

# I will build the site on Wordpress

# Designs will need to include responsiveness

Target Market(s)

Business Owners who want to upgrade to a POS System to increase productivity

Industry/Entity Type

Industry

Requirements
Must have
• Menu as above
Responsive Design

```html
<!DOCTYPE html>
<html lang="en">
<head>
<meta charset="utf-8">
<title>Brindle Checkout – Point of Sale Solutions</title>
<link rel="stylesheet" href="https://fonts.googleapis.com/css2?family=Arimo:ital,wght@0,400;0,700;1,400&display=swap">
<style>
:root{
  --brand-blue:#4a56b4;
  --brand-blue-dark:#3e4aa3;
  --sky:#1ea3f0;
  --sky-dark:#168fd8;
  --green:#7bc143;
  --green-dark:#67ad33;
  --page:#f0f0f0;
  --panel:#ffffff;
  --ink:#333333;
  --muted:#777777;
  --line:#e4e4e4;
  --charcoal:#4a4a4a;
}
*{box-sizing:border-box;margin:0;padding:0}
html,body{width:1200px;height:1164px;overflow:hidden}
body{position:relative;background:var(--page);font-family:"Arimo",Arial,sans-serif;color:var(--ink)}
a{color:inherit;text-decoration:none}
.abs{position:absolute}

.header-band{left:0;top:0;width:1200px;height:338px;background:radial-gradient(circle at 85% 20%,#5561c0 0,var(--brand-blue) 40%,var(--brand-blue-dark) 100%)}

.brand{left:236px;top:44px;color:#fff}
.brand-name{display:flex;align-items:center;gap:10px;font-size:40px;font-weight:400;letter-spacing:1px}
.brand-mark{width:26px;height:26px;border-radius:50%;background:#fff}
.brand-tag{font-size:16px;margin-top:6px;color:#e8ebff}

.top-links{left:656px;top:35px;display:flex;gap:22px;font-size:7.5px;font-weight:700;text-transform:uppercase;color:#9fd6ff}
.top-links .current{color:#fff}
.top-links .lang{color:#fff;margin-left:16px}

.phone{left:530px;top:87px;display:flex;align-items:center;gap:12px;color:#fff;font-size:21px}
.search{left:690px;top:86px;width:145px;height:25px;background:var(--green);display:flex;align-items:center;justify-content:space-between;padding:0 9px;font-size:8px;color:#2f5a12}
.cart{left:849px;top:86px;width:132px;height:25px;background:var(--sky);display:flex;align-items:center;gap:6px;padding:0 8px;font-size:7.5px;color:#fff}
.cart b{font-weight:700}
.cart .total{color:#cfeeff}

.main-nav{left:236px;top:163px;width:745px;height:35px;background:var(--sky);display:flex}
.main-nav a{flex:auto;display:flex;align-items:center;justify-content:center;font-size:8.5px;font-weight:700;color:#fff;text-transform:uppercase;border-right:1px solid rgba(255,255,255,.3)}
.main-nav a:last-child{border-right:0}

.panel{background:var(--panel)}
.categories{left:236px;top:204px;width:128px;height:259px;padding:7px}
.panel-head{height:28px;background:linear-gradient(var(--sky),var(--sky-dark));color:#fff;font-size:9px;font-weight:700;display:flex;align-items:center;padding-left:8px;font-variant:small-caps;letter-spacing:.3px}
.cat-list{list-style:none;padding:4px 1px}
.cat-list li{font-size:7px;font-weight:700;color:#666;height:22.3px;display:flex;align-items:center;border-bottom:1px solid var(--line)}
.cat-list li:last-child{border:0}
.cat-list li.active{color:var(--green)}

.hero{left:372px;top:204px;width:609px;height:260px;background:radial-gradient(circle at 30% 45%,#6dbb3a 0,#c8472c 22%,#d9eef2 45%,#ffffff 75%)}
.hero-caption{left:680px;top:379px;width:230px;height:85px;background:rgba(40,40,40,.82);padding:14px 26px;color:#fff}
.hero-caption::before{content:"";position:absolute;left:20px;top:-1px;border:8px solid transparent;border-top-color:var(--sky)}
.hero-caption h2{font-size:12.5px;font-weight:400;margin-bottom:6px}
.hero-caption p{font-size:7.5px;line-height:1.7;color:#ddd}
.hero-caption span{color:var(--sky)}

.my-cart{left:236px;top:471px;width:128px;height:74px;background:var(--sky);color:#fff}
.my-cart .panel-head{height:26px;background:linear-gradient(#3d97e3,#2a7fd0)}
.my-cart p{font-size:7.5px;line-height:1.5;padding:10px 14px}

.side-links{left:236px;top:552px;width:128px;height:188px;padding:16px 10px}
.side-title{font-size:9px;color:#333;font-variant:small-caps;padding-bottom:8px;border-bottom:1px solid var(--line);margin-bottom:12px}
.side-list{list-style:none}
.side-list li{display:flex;align-items:center;gap:7px;font-size:7px;font-weight:700;color:#555;height:17px}
.side-list li.active{color:var(--green)}
.dot{width:8px;height:8px;border-radius:50%;background:#bbb;position:relative}
.dot::after{content:"";position:absolute;left:3px;top:2px;border:2px solid transparent;border-left:3px solid #fff}
.btn-dark{display:inline-block;background:var(--charcoal);color:#fff;font-size:7px;font-weight:700;padding:8px 13px;margin-top:20px}

.side-text{left:236px;top:752px;width:128px;height:135px;padding:16px 10px}
.side-text p{font-size:7px;line-height:1.75;color:#888}

.industries{left:372px;top:473px;width:609px;display:flex;gap:8px}
.industry{width:146.25px;height:145px;background:var(--panel);padding:0 14px;text-align:center}
.industry h3{font-size:8.5px;font-weight:400;color:#555;height:40px;line-height:43px;border-bottom:1px solid var(--line);margin-bottom:10px}
.industry.featured h3{color:var(--green)}
.industry-image{height:90px}
.industry-promo{height:90px;background:var(--green);color:#fff;text-align:left;padding:18px 12px;font-size:8px;font-weight:700;line-height:1.4}
.industry-promo a{display:inline-block;margin-top:12px;font-size:7.5px;text-decoration:underline}

.call-bar{left:372px;top:634px;width:609px;height:53px;background:var(--panel);display:flex;align-items:center;padding-left:53px;gap:46px;font-size:13.5px;color:#444}
.call-bar strong{color:var(--green)}
.call-bar .btn-dark{margin:0;font-size:8.5px;padding:10px 24px}

.videos-title{left:372px;top:710px;width:609px;font-size:10px;color:#555;padding-bottom:7px;border-bottom:1px solid #ddd}
.videos{left:372px;top:740px;width:609px;display:flex;gap:8px}
.video{width:146.25px;height:146px;background:var(--panel)}
.video-frame{height:105px;background:linear-gradient(#1d1f3e,#3a2a4a 55%,#141414);position:relative}
.video-frame .play{position:absolute;left:63px;top:44px;width:18px;height:14px;border-radius:3px;background:rgba(0,0,0,.7)}
.video-frame .play::after{content:"";position:absolute;left:7px;top:3px;border:4px solid transparent;border-left:6px solid #fff}
.video-meta{padding:10px 9px}
.video-meta h4{font-size:7.5px;font-weight:400;color:#333}
.video-meta p{font-size:6px;color:#888;margin-top:5px}
.video.active h4{color:var(--green);text-decoration:underline}
.video.active p{color:var(--green);font-style:italic}

.footer-band{left:236px;top:910px;width:745px;height:199px;background:var(--panel);display:flex}
.testimonial{width:245px;background:var(--green);color:#fff;padding:24px 22px;position:relative}
.testimonial h3{font-size:13px;font-weight:400;padding-bottom:9px;border-bottom:1px solid rgba(255,255,255,.35);margin-bottom:8px}
.quote-mark{position:absolute;right:24px;top:18px;width:30px;height:26px;display:flex;gap:5px}
.quote-mark i{flex:1;background:rgba(255,255,255,.4);border-radius:2px 2px 8px 2px}
.testimonial .date{font-size:6px;font-style:italic}
.testimonial .who{font-size:7.5px;font-weight:700;margin:10px 0 8px}
.testimonial p{font-size:7px;line-height:1.7}
.btn-light{display:inline-block;background:#fff;color:#666;font-size:7.5px;padding:8px 13px;margin-top:12px;border:1px solid #ddd}
.about,.subscribe{padding:24px 22px}
.about{width:248px}
.subscribe{flex:1}
.footer-band h3{font-size:13px;font-weight:400;color:#444;padding-bottom:10px;border-bottom:1px solid var(--line);margin-bottom:14px}
.about h4{font-size:7.5px;color:#555;margin-bottom:14px}
.about p{font-size:7px;line-height:1.75;color:#888}
.subscribe .hint{font-size:6px;font-style:italic;color:#777;margin-bottom:16px}
.subscribe-form{display:flex}
.subscribe-form span{width:137px;height:25px;border:1px solid var(--line)}
.subscribe-form b{width:48px;height:25px;background:var(--green);color:#fff;font-size:8px;font-style:italic;display:flex;align-items:center;justify-content:center}

.legal{left:236px;top:1130px;font-size:7.5px;color:#777}
.legal b{color:#555}
.social{left:886px;top:1124px;display:flex;gap:6px}
.social span{width:20px;height:20px;background:#2d2d2d;display:flex;align-items:center;justify-content:center}
</style>
</head>
<body>
<div class="abs header-band"></div>

<div class="abs brand">
  <div class="brand-name"><span class="brand-mark"></span>Brindle Checkout</div>
  <div class="brand-tag">Brindle Point of Sale Solutions</div>
</div>

<nav class="abs top-links">
  <a class="current">Home</a><a>My Account</a><a>Shopping Cart</a><a>Login</a><a>Create Account</a><a class="lang">EN ▾</a>
</nav>

<div class="abs phone">
  <svg width="13" height="17" viewBox="0 0 13 17"><path d="M3 1 L5.5 1 L6.5 5 L4.5 6.5 Q6 10.5 8.5 12.5 L10.5 11 L12.5 13.5 L11 16 Q4 14 1 4 Z" fill="#fff"/></svg>
  1300 555 218
</div>
<div class="abs search"><span>SEARCH</span>
  <svg width="10" height="10" viewBox="0 0 10 10"><circle cx="4" cy="4" r="3" stroke="#fff" stroke-width="1.5" fill="none"/><path d="M6.2 6.2 9 9" stroke="#fff" stroke-width="1.6"/></svg>
</div>
<div class="abs cart">
  <svg width="12" height="10" viewBox="0 0 12 10"><path d="M0 1h2l2 6h6l1.5-4.5H3" stroke="#fff" fill="none" stroke-width="1.2"/><circle cx="5" cy="9" r="1" fill="#fff"/><circle cx="9" cy="9" r="1" fill="#fff"/></svg>
  <b>CART</b><span class="total">0 ITEM(S) - $0.00</span><span style="margin-left:auto">▾</span>
</div>

<nav class="abs main-nav">
  <a style="width:113px">Our Products</a><a>About Us</a><a style="width:134px">Company Events</a><a>Testimonial</a><a>Gallery</a><a>Sitemap</a><a style="width:117px">Contact Us</a>
</nav>

<aside class="abs panel categories">
  <div class="panel-head">Categories</div>
  <ul class="cat-list">
    <li>Lorem ipsum dolor</li><li>Lorem sit amet</li><li>Lorem ipsum dolor</li><li>Lorem ipsum sit amet</li><li>Lorem ipsum dolor</li><li>Lorem ipsum dolor</li><li class="active">Lorem ipsum</li><li>Lorem ipsum sit</li>
  </ul>
</aside>

<div class="abs hero" role="img" aria-label="Red and green apples splashing into clear water"></div>
<div class="abs hero-caption">
  <h2>Lorem ipsum dolor sit</h2>
  <p>Lorem ipsum dolor sit amet, consectetur adipiscing elit, sed do <span>eiusmod tempor incididunt</span> ut labore et dolore magna aliqua.</p>
</div>

<aside class="abs my-cart">
  <div class="panel-head">My Cart</div>
  <p>You have no item in your shopping cart</p>
</aside>

<aside class="abs panel side-links">
  <div class="side-title">Lorem Ipsum</div>
  <ul class="side-list">
    <li class="active"><i class="dot"></i>Lorem ipsum</li><li><i class="dot"></i>Lorem ipsum sit</li><li><i class="dot"></i>Lorem  dolor sit</li><li><i class="dot"></i>Lorem ipsum</li><li><i class="dot"></i>Lorem ipsum dolor sit</li>
  </ul>
  <a class="btn-dark">VIEW ALL</a>
</aside>

<aside class="abs panel side-text">
  <div class="side-title">Lorem Ipsum</div>
  <p>Lorem ipsum dolor sit amet, consectetur adipiscing elit, sed do eiusmod tempor incididunt ut labore et dolore magna aliqua.</p>
</aside>

<section class="abs industries">
  <div class="industry featured"><h3>Restaurants and Cafes</h3>
    <div class="industry-promo">Lorem ipsum dolor sit amet, consectetur adipi-sicing elit<br><a>continue &gt;&gt;</a></div>
  </div>
  <div class="industry"><h3>Bars and Clubs</h3><div class="industry-image" role="img" aria-label="Black and white nightclub crowd under stage lights" style="background:radial-gradient(circle at 50% 30%,#cfcfcf,#2a2a2a 60%,#111)"></div></div>
  <div class="industry"><h3>Grocery and Convenience</h3><div class="industry-image" role="img" aria-label="Black and white convenience store front" style="background:linear-gradient(#9a9a9a,#3a3a3a 55%,#bdbdbd)"></div></div>
  <div class="industry"><h3>Fruit and Veg</h3><div class="industry-image" role="img" aria-label="Black and white pile of fresh fruit and vegetables" style="background:radial-gradient(circle at 50% 60%,#a9a9a9,#555 70%)"></div></div>
</section>

<div class="abs call-bar">
  <span>CALL <strong>1300 555 218</strong> to speak to an incredibly friendly staff.</span>
  <a class="btn-dark">CONTACT US</a>
</div>

<h2 class="abs videos-title" style="font-weight:400">Lorem Ipsum</h2>
<section class="abs videos">
  <article class="video active"><div class="video-frame" role="img" aria-label="Video testimonial filmed in a bar"><span class="play"></span></div><div class="video-meta"><h4>Heading Here</h4><p>Monday, 19 Sep 2011 17:08 - Lena Morrow</p></div></article>
  <article class="video"><div class="video-frame" role="img" aria-label="Video testimonial filmed in a bar"><span class="play"></span></div><div class="video-meta"><h4>Heading Here</h4><p>Monday, 19 Sep 2011 17:08 - Lena Morrow</p></div></article>
  <article class="video"><div class="video-frame" role="img" aria-label="Video testimonial filmed in a bar"><span class="play"></span></div><div class="video-meta"><h4>Heading Here</h4><p>Monday, 19 Sep 2011 17:08 - Lena Morrow</p></div></article>
  <article class="video"><div class="video-frame" role="img" aria-label="Video testimonial filmed in a bar"><span class="play"></span></div><div class="video-meta"><h4>Heading Here</h4><p>Monday, 19 Sep 2011 17:08 - Lena Morrow</p></div></article>
</section>

<footer class="abs footer-band">
  <div class="testimonial">
    <div class="quote-mark"><i></i><i></i></div>
    <h3>Testimonial</h3>
    <div class="date">Date: May 11, 2010</div>
    <div class="who">Dana Whitmore - TRAIL STORES</div>
    <p>We have five TRAIL store outlet accross Perth WA. In 2002 we approached TILL &amp; TRADE to supply our POS Solutions for all our stores. They exceeded all our expectations with their prompt, professional</p>
    <a class="btn-light">View More</a>
  </div>
  <div class="about">
    <h3>About Us</h3>
    <h4>Heading for about us</h4>
    <p>Lorem ipsum dolor sit amet, consectetur adipiscing elit, sed do eiusmod tempor incididunt ut labore et dolore magna aliqua. Ut enim ad minim veniam, quis nostrud exercitation ullamco laboris nisi ut aliquip ex ea commodo consequat.</p>
    <a class="btn-light" style="margin-top:20px">Read More</a>
  </div>
  <div class="subscribe">
    <h3>Subscribe</h3>
    <div class="hint">Enter Your Email For Subscribe</div>
    <div class="subscribe-form"><span></span><b>SEND</b></div>
  </div>
</footer>

<div class="abs legal"><b>COMPANY NAME</b> © 2014 | PRIVACY POLICY</div>
<div class="abs social">
  <span></span><span></span><span></span>
  <span><svg width="10" height="10" viewBox="0 0 10 10"><path d="M5 1v8M1 5h8" stroke="#fff" stroke-width="2"/></svg></span>
</div>
</body>
</html>
```